Wooden Floor Website

I'd like a Modern and crisp site with emphasis on the site being easy to navigate through - services that we offer, gallery of previous work, history, who we are, contact, etc
https://vaultqx8261937-my.filedeckly.com/:b:/g/personal/tobias_pellwickhaus_co_uk/QWM7R2_kpLsTbNVafrxHoZWCKdYeP8u3G6vRPMsLmoXBtc

Coded - Design and coding required

5+ page

• Word Press Site

```html
<!DOCTYPE html>
<html lang="en">
<head>
<meta charset="utf-8">
<title>Pellwick Haus — Bespoke Wood Flooring</title>
<link rel="stylesheet" href="https://fonts.googleapis.com/css2?family=Poppins:wght@300;400;600;700&family=Lato:wght@400;700&display=swap">
<style>
:root{
  --page:#f5f5f5;
  --ink:#1f1f1f;
  --muted:#555;
  --line:#222;
  --footer:#141414;
  --footer-text:#e8e8e8;
  --white:#ffffff;
  --oak-light:#d9d3cb;
  --oak-mid:#8a6a4e;
  --oak-dark:#4d3b2d;
}
*{box-sizing:border-box;margin:0;padding:0}
html,body{width:1200px;height:3854px;overflow:hidden;background:var(--page)}
body{position:relative;font-family:"Lato",sans-serif;color:var(--ink)}
.abs{position:absolute}
.heading{font-family:"Poppins",sans-serif;font-weight:400;color:var(--ink)}

/* header */
.site-header{left:0;top:0;width:1200px;height:123px;background:var(--page)}
.brand{left:82px;top:40px;width:150px;text-align:center;font-family:"Lato",sans-serif;font-weight:700;font-size:15px;letter-spacing:1px;color:var(--ink)}
.brand-mark{display:block;width:44px;height:44px;margin:0 auto 8px;border:2px solid var(--ink)}
.main-nav{left:462px;top:56px;display:flex;gap:32px;font-size:15px}
.main-nav a{color:var(--ink);text-decoration:none}
.main-nav a.current{font-weight:700;border-bottom:2px solid var(--ink);padding-bottom:3px}
.social{display:flex;gap:9px}
.social span{width:24px;height:24px;border-radius:50%;background:var(--ink)}
.header-social{left:994px;top:54px}

/* hero */
.hero{left:0;top:123px;width:1200px;height:630px;background:linear-gradient(120deg,#e3dcd4 0%,#ece7e1 45%,#dcd6cf 100%)}
.hero-accent{left:0;top:123px;width:520px;height:420px;background:radial-gradient(ellipse at 40% 45%,#d8a898 0%,#d3a292 45%,rgba(220,214,207,0) 72%)}
.hero-title{left:0;top:418px;width:1200px;text-align:center;font-family:"Poppins",sans-serif;font-weight:700;font-size:31px;line-height:39px;color:var(--white);letter-spacing:1px;text-shadow:0 1px 3px rgba(0,0,0,.25)}
.hero-btn{left:514px;top:509px;width:144px;height:31px;border:1px solid var(--white);color:var(--white);font-size:12px;display:flex;align-items:center;justify-content:center}
.hero-arrow{top:422px}
.hero-dots{left:552px;top:715px;display:flex;gap:8px}
.hero-dots span{width:18px;height:3px;background:rgba(255,255,255,.7)}
.hero-dots span.on{background:var(--ink)}

/* buttons */
.btn{height:36px;border:2px solid var(--line);display:flex;align-items:center;justify-content:center;font-size:12px;color:var(--ink)}
.btn::before,.btn::after{content:"";position:absolute;left:-22px;right:-22px;height:2px;background:var(--line)}
.btn::before{top:-2px}
.btn::after{bottom:-2px}

/* sections */
.section-title{width:1200px;left:0;text-align:center;font-size:31px}
.services-intro{left:0;top:858px;width:1200px;text-align:center;font-size:13px;line-height:19px;color:var(--muted)}
.photo{display:block}
.service-label{top:1180px;text-align:center;font-size:17px;letter-spacing:.5px}

.copy{font-size:13px;line-height:17px;color:var(--muted)}
.rule{height:2px;background:var(--line)}

/* contact */
.field{border:2px solid var(--line);background:var(--page);font-size:12px;padding:7px 12px;color:var(--ink)}

/* footer */
.site-footer{left:0;top:3495px;width:1200px;height:303px;background:var(--footer);color:var(--footer-text)}
.footer-brand{left:82px;top:3600px;width:130px;text-align:center;font-weight:700;font-size:15px;letter-spacing:1px;color:var(--footer-text)}
.footer-brand .brand-mark{border-color:var(--footer-text)}
.footer-head{font-size:14px;color:var(--footer-text)}
.footer-list{list-style:disc;padding-left:18px;font-size:13px;line-height:20px;color:var(--footer-text)}
.footer-contact{font-size:13px;line-height:20px;color:var(--footer-text)}
.footer-contact td{vertical-align:top;padding-right:14px}
.sub-input{left:845px;top:3649px;width:270px;height:36px;background:#2e2e2e;color:#9a9a9a;font-size:12px;display:flex;align-items:center;justify-content:center}
.sub-btn{left:845px;top:3695px;width:270px;height:36px;background:var(--white);color:var(--ink);font-weight:700;font-size:15px;display:flex;align-items:center;justify-content:center}
.bottom-bar{left:0;top:3798px;width:1200px;height:56px;background:var(--page)}
.copyright{left:80px;top:3818px;font-size:12px;color:var(--ink)}
.footer-social{left:955px;top:3814px}
</style>
</head>
<body>

<header class="site-header abs">
  <div class="brand abs"><span class="brand-mark"></span>PELLWICK HAUS</div>
  <nav class="main-nav abs">
    <a class="current" href="#">Home</a><a href="#">About us</a><a href="#">Serivcrs</a><a href="#">Gallery</a><a href="#">History</a><a href="#">Contact us</a>
  </nav>
  <div class="social header-social abs"><span></span><span></span><span></span><span></span></div>
</header>

<section class="hero abs" role="img" aria-label="Pale oak herringbone floor with a coral side table, vase of dried branches and sketchbook"></section>
<div class="hero-accent abs"></div>
<h1 class="hero-title abs">CREATING YOUR EXCEPTIONAL<br>WOOD FLOOR</h1>
<div class="hero-btn abs">Read More</div>
<svg class="hero-arrow abs" style="left:38px" width="16" height="28" viewBox="0 0 16 28"><path d="M14 2 L3 14 L14 26" fill="none" stroke="#fff" stroke-width="3"/></svg>
<svg class="hero-arrow abs" style="left:1146px" width="16" height="28" viewBox="0 0 16 28"><path d="M2 2 L13 14 L2 26" fill="none" stroke="#fff" stroke-width="3"/></svg>
<div class="hero-dots abs"><span></span><span class="on"></span><span></span><span></span></div>

<!-- services -->
<h2 class="heading section-title abs" style="top:815px">Services</h2>
<p class="services-intro abs">PELLWICK HAUS offer a range of fully bespoke finished<br>wood flooring in planks,</p>
<div class="photo abs" style="left:82px;top:925px;width:242px;height:234px;background:linear-gradient(160deg,#6d4a30,#9a6e48)" role="img" aria-label="Hands laying a wooden plank"></div>
<div class="photo abs" style="left:347px;top:925px;width:241px;height:234px;background:linear-gradient(160deg,#e9e6e1,#6f6a64)" role="img" aria-label="Grey herringbone blocks beside a white skirting board"></div>
<div class="photo abs" style="left:612px;top:925px;width:244px;height:234px;background:linear-gradient(180deg,#9fb89a,#4a4a48 55%,#3b3b3a)" role="img" aria-label="Dark chevron floor by a garden window"></div>
<div class="photo abs" style="left:879px;top:925px;width:241px;height:234px;background:linear-gradient(180deg,#2d2d2d 0%,#3a3530 45%,#8a6540 100%)" role="img" aria-label="Herringbone floor in a styled interior"></div>
<div class="service-label abs heading" style="left:82px;width:242px">Wood Flooring</div>
<div class="service-label abs heading" style="left:347px;width:241px">Herringbone Blocks</div>
<div class="service-label abs heading" style="left:612px;width:244px">Chevrons</div>
<div class="service-label abs heading" style="left:879px;width:241px">Interior Design</div>
<div class="btn abs" style="left:509px;top:1254px;width:198px">Read More</div>

<!-- gallery -->
<h2 class="heading section-title abs" style="top:1326px">Gallery</h2>
<div class="photo abs" style="left:80px;top:1537px;width:326px;height:249px;background:linear-gradient(180deg,#d8d2c8,#4a3f36)" role="img" aria-label="Kitchen with dark wood floor and dining chairs"></div>
<div class="photo abs" style="left:80px;top:1814px;width:326px;height:247px;background:linear-gradient(135deg,#8c8177,#b7aca1)" role="img" aria-label="Grey herringbone floor close-up"></div>
<div class="photo abs" style="left:434px;top:1398px;width:327px;height:249px;background:linear-gradient(180deg,#3e5240,#7a5034 40%,#5a3a26)" role="img" aria-label="Wood floor with a wire side table and plant"></div>
<div class="photo abs" style="left:434px;top:1670px;width:327px;height:250px;background:linear-gradient(180deg,#1f4a5c 0%,#2a5566 40%,#b07a4e 60%,#a06c44)" role="img" aria-label="Bedroom with teal wall and herringbone floor"></div>
<div class="photo abs" style="left:434px;top:1940px;width:327px;height:252px;background:linear-gradient(180deg,#2a2826,#4f4038)" role="img" aria-label="Dark herringbone floor with plant pot"></div>
<div class="photo abs" style="left:786px;top:1537px;width:329px;height:249px;background:linear-gradient(135deg,#c8b9a6,#b29e86)" role="img" aria-label="Light oak planks with a small table"></div>
<div class="photo abs" style="left:786px;top:1814px;width:329px;height:247px;background:linear-gradient(135deg,#9d7651,#c19a70)" role="img" aria-label="Natural oak herringbone close-up"></div>
<div class="btn abs" style="left:509px;top:2236px;width:198px">Read More</div>

<!-- history -->
<h2 class="heading abs" style="left:131px;top:2400px;font-size:31px">History</h2>
<div class="rule abs" style="left:131px;top:2449px;width:72px"></div>
<p class="copy abs" style="left:131px;top:2470px;width:420px">Lorem Ipsum is simply dummy text of the printing and wood typesetting industry.</p>
<p class="copy abs" style="left:131px;top:2516px;width:420px">Lorem Ipsum has been the industry's standard dummy text a ever since the 1500s, when an unknown printer took a galley of type and scrambled it to make a type specimen book</p>
<div class="btn abs" style="left:103px;top:2600px;width:195px">Read More</div>
<div class="photo abs" style="left:727px;top:2326px;width:363px;height:293px;background:linear-gradient(135deg,#cfc4b6,#b3a594)" role="img" aria-label="Pale oak planks"></div>
<div class="photo abs" style="left:576px;top:2418px;width:362px;height:303px;background:linear-gradient(160deg,#9cbf4a,#4e7a2a 55%,#3b4a22)" role="img" aria-label="Old oak tree in a forest"></div>

<!-- who we are -->
<div class="photo abs" style="left:80px;top:2816px;width:167px;height:134px;background:linear-gradient(135deg,#c8b08a,#8a7858)" role="img" aria-label="Craftsman sanding a wood block"></div>
<div class="photo abs" style="left:80px;top:2976px;width:167px;height:133px;background:linear-gradient(135deg,#d4c7b4,#9a7f63)" role="img" aria-label="Stacked timber boards"></div>
<div class="photo abs" style="left:270px;top:2816px;width:362px;height:293px;background:linear-gradient(180deg,#c9c6bf,#7d7a72 60%,#55524c)" role="img" aria-label="Workers in a flooring workshop"></div>
<div class="abs" style="left:689px;top:2822px;font-size:12px;color:var(--muted)">About us</div>
<h2 class="heading abs" style="left:689px;top:2836px;font-size:31px">who we are</h2>
<div class="rule abs" style="left:689px;top:2884px;width:72px"></div>
<p class="copy abs" style="left:689px;top:2894px;width:420px">Lorem Ipsum is simply dummy text of the printing and wood typesetting industry.</p>
<p class="copy abs" style="left:689px;top:2940px;width:420px">Lorem Ipsum has been the industry's standard dummy text a ever since the 1500s, when an unknown printer took a galley of type and scrambled it to make a type specimen book</p>
<div class="btn abs" style="left:686px;top:3024px;width:175px">Read More</div>

<!-- contact -->
<h2 class="heading section-title abs" style="top:3157px">Contact us</h2>
<div class="field abs" style="left:270px;top:3214px;width:203px;height:39px">Name</div>
<div class="field abs" style="left:496px;top:3214px;width:203px;height:39px">Phone</div>
<div class="field abs" style="left:722px;top:3214px;width:203px;height:39px">Email</div>
<div class="field abs" style="left:270px;top:3269px;width:655px;height:113px">Message</div>
<div class="btn abs" style="left:509px;top:3412px;width:198px">Read More</div>

<!-- footer -->
<footer class="site-footer abs"></footer>
<div class="footer-brand brand abs" style="top:3600px"><span class="brand-mark"></span>PELLWICK HAUS</div>
<div class="footer-head abs" style="left:316px;top:3570px">Quick Link</div>
<ul class="footer-list abs" style="left:322px;top:3615px">
  <li>Home</li><li>About us</li><li>Serivcrs</li><li>Gallery</li><li>History</li><li>Contact us</li>
</ul>
<div class="footer-head abs" style="left:504px;top:3570px">Contact us</div>
<table class="footer-contact abs" style="left:504px;top:3613px">
  <tr><td>A :</td><td>123th Street,<br>City, UK</td></tr>
  <tr><td>P:</td><td>+44 (0)20 7946 0312<br>+44 (0)7700 900 481</td></tr>
  <tr><td>E:</td><td>enquire@pellwickhaus.co.uk</td></tr>
</table>
<div class="footer-head abs" style="left:840px;top:3570px">Subscribe to our newsletter</div>
<div class="abs" style="left:845px;top:3620px;font-size:12px;color:var(--footer-text)">To receive the latest news &amp; update</div>
<div class="sub-input abs">Email Here</div>
<div class="sub-btn abs">Submit</div>

<div class="bottom-bar abs"></div>
<div class="copyright abs">Copyright © Pellwick Haus. All Right Reserved</div>
<div class="social footer-social abs"><span></span><span></span><span></span><span></span><span></span></div>

</body>
</html>
```